Solar appointment reminder card

We are looking for a new design for our appointment reminder card since we have changed our logo. The card should have the new logo along with space for the employee to hand write the customers appointment date, time, the employees name and phone number.
I've uploaded what our old basic appointment card looked like and our new logo.

The cards should be in a standard business card size and could be horizontal or vertical.

```html
<!DOCTYPE html>
<html lang="en">
<head>
<meta charset="utf-8">
<title>Appointment Reminder Card</title>
<link href="https://fonts.googleapis.com/css2?family=EB+Garamond:ital,wght@0,400;0,600;1,600&display=swap" rel="stylesheet">
<style>
  :root {
    --page: #ffffff;
    --brand-orange: #f15123;
    --card-dark: #211418;
    --logo-panel: #231f20;
    --logo-gold: #f7941d;
    --logo-sun: #fcc22b;
    --text-light: #ffffff;
    --field-fill: #ffffff;
    --field-edge: #d9d9d9;
  }
  * { margin: 0; padding: 0; box-sizing: border-box; }
  html, body {
    width: 1200px;
    height: 714px;
    overflow: hidden;
    background: var(--page);
  }
  .card {
    position: absolute;
    left: 32px;
    top: 31px;
    width: 1136px;
    height: 649px;
    background: var(--card-dark);
    box-shadow: 0 2px 8px rgba(0, 0, 0, 0.45);
    font-family: "EB Garamond", Garamond, serif;
    color: var(--text-light);
    overflow: hidden;
  }
  .brand-band {
    position: absolute;
    left: 0;
    top: 0;
    width: 334px;
    height: 100%;
    background: var(--brand-orange);
  }
  .brand-plate {
    position: absolute;
    left: 0;
    top: 262px;
    width: 298px;
    height: 160px;
    background: var(--logo-panel);
    border-radius: 0 10px 10px 0;
    display: flex;
    align-items: center;
    justify-content: center;
    gap: 12px;
  }
  .brand-dot {
    width: 30px;
    height: 30px;
    border-radius: 50%;
    background: var(--logo-sun);
    flex: none;
  }
  .brand-name {
    font-weight: 600;
    font-size: 34px;
    color: var(--logo-gold);
    letter-spacing: 0.5px;
    white-space: nowrap;
  }
  .card-title {
    position: absolute;
    left: 334px;
    right: 0;
    top: 38px;
    text-align: center;
    font-style: italic;
    font-weight: 600;
    font-size: 78px;
    line-height: 1;
    letter-spacing: 1px;
  }
  .fields {
    position: absolute;
    left: 352px;
    top: 172px;
    list-style: none;
  }
  .field {
    position: relative;
    height: 92.4px;
    width: 760px;
  }
  .field-label {
    position: absolute;
    left: 0;
    top: 2px;
    font-size: 37px;
    line-height: 1;
    letter-spacing: 0.5px;
  }
  .field-colon {
    position: absolute;
    left: 240px;
    top: 8px;
    font-size: 30px;
    line-height: 1;
  }
  .field-line {
    position: absolute;
    left: 274px;
    top: 0;
    width: 486px;
    height: 63px;
    background: var(--field-fill);
    border: 1px solid var(--field-edge);
    border-radius: 13px;
  }
</style>
</head>
<body>
  <main class="card">
    <section class="brand-band">
      <div class="brand-plate">
        <span class="brand-dot" aria-hidden="true"></span>
        <span class="brand-name">Sunridge Solar</span>
      </div>
    </section>

    <h1 class="card-title">Appointment</h1>

    <ul class="fields">
      <li class="field"><span class="field-label">Name</span><span class="field-colon">:</span><span class="field-line"></span></li>
      <li class="field"><span class="field-label">Date</span><span class="field-colon">:</span><span class="field-line"></span></li>
      <li class="field"><span class="field-label">Time</span><span class="field-colon">:</span><span class="field-line"></span></li>
      <li class="field"><span class="field-label">Representative</span><span class="field-colon">:</span><span class="field-line"></span></li>
      <li class="field"><span class="field-label">Phone</span><span class="field-colon">:</span><span class="field-line"></span></li>
    </ul>
  </main>
</body>
</html>
```